New telco company needs a product page

We need to design two pages - one index and one inner.

We are a new telco company and we have developed our own phone. We will be selling our services and the phone on this site.

The design should be easy to understand and use, following the latest trends in Web design, be clean. It should communicate professionalism and integrity.

The name of our company is VORO which stands for Value Over Rush Often. The design should follow this principle.

Our company logo is attached. I can send it in other colors/sizes - let me know.

Target Market(s)

Aging population (70+), middle-aged with parents and grandparents.

Industry/Entity Type

It Company

Requirements
Must have
• index page, inner page, flat, clean, Pellucor 5 style / ZEB style (quintel.example), easy navigation, fluid layout, CSS, tableless
Should not have
• should not use old fonts, should not use old-style design, should not have animation, should not look like QDX or Bimzo (too busy)

```html
<!DOCTYPE html>
<html lang="en">
<head>
<meta charset="utf-8">
<title>VORO — Telecom Services</title>
<link href="https://fonts.googleapis.com/css2?family=Ubuntu:wght@300;400&display=swap" rel="stylesheet">
<style>
:root{
  --ink:#1f1f1f;
  --text:#5e5e5e;
  --muted:#8a8a8a;
  --line:#d9d9d9;
  --nav-top:#fbfbfb;
  --nav-bottom:#e9e9e9;
  --hero-top:#ffffff;
  --hero-bottom:#e7e7e7;
  --social-grey:#b4b4b4;
  --social-blue:#3a8fd4;
  --footer-bg:#f3f3f3;
}
*{box-sizing:border-box;margin:0;padding:0}
html,body{width:1138px;height:1200px;overflow:hidden;background:#fff}
body{position:relative;font-family:"Ubuntu",sans-serif;color:var(--text)}
.hero-band{position:absolute;left:0;top:0;width:1138px;height:606px;
  background:linear-gradient(to bottom,var(--hero-top) 0%,#fafafa 70%,var(--hero-bottom) 100%);
  border-bottom:1px solid #e2e2e2}
.brand{position:absolute;left:103px;top:38px;font-weight:300;font-size:58px;line-height:64px;letter-spacing:1px;color:var(--ink)}
.social-top{position:absolute;left:915px;top:91px;display:flex;gap:4px}
.social-top span{width:24px;height:24px;border-radius:50%;background:var(--social-grey)}
.main-nav{position:absolute;left:102px;top:135px;width:934px;height:52px;display:flex;
  border:1px solid #cfcfcf;border-radius:3px;
  background:linear-gradient(to bottom,var(--nav-top),var(--nav-bottom))}
.main-nav a{display:flex;align-items:center;justify-content:center;height:100%;
  font-size:15px;color:#444;text-decoration:none;border-right:1px solid #cfcfcf}
.main-nav a:last-child{border-right:none}
.hero-title{position:absolute;left:134px;top:286px;white-space:nowrap;font-weight:400;font-size:36px;line-height:44px;color:var(--ink);letter-spacing:-.2px}
.hero-sub{position:absolute;left:135px;top:335px;white-space:nowrap;font-weight:300;font-size:22px;line-height:28px;color:#2a2a2a}
.hero-text{position:absolute;left:136px;top:372px;width:400px;font-weight:300;font-size:12.5px;line-height:20px;color:var(--text)}
.pager{position:absolute;left:135px;top:427px;display:flex;gap:3px}
.pager span{width:12px;height:12px;border-radius:50%;background:#d2d2d2}
.pager span.active{background:#9a9a9a}
.arrow{position:absolute;top:316px}
.arrow.prev{left:74px}.arrow.next{left:1025px}
.hero-visual{position:absolute;left:602px;top:192px;width:378px;height:360px;
  background:radial-gradient(ellipse at 55% 50%,#cfd9e6 0%,#e9edf2 45%,#f7f7f7 75%,rgba(255,255,255,0) 100%)}
.cards{position:absolute;left:107px;top:641px;display:flex;gap:10px}
.card{width:226px;height:188px;border:1px solid #e0e0e0;border-radius:4px;background:#fff;
  box-shadow:0 1px 2px rgba(0,0,0,.05);padding:13px 12px 0 12px}
.card .thumb{width:205px;height:106px;border-radius:2px}
.card h3{font-weight:400;font-size:15.5px;color:var(--ink);margin:13px 0 0 5px;line-height:20px}
.card p{font-weight:300;font-size:12px;color:var(--muted);margin:2px 0 0 5px;white-space:nowrap}
.thumb.office{background:linear-gradient(120deg,#b5523d,#d9a58c 50%,#4a3a33)}
.thumb.support{background:linear-gradient(110deg,#c89a78,#ecd7c4 55%,#dcdcdc)}
.thumb.handsets{background:linear-gradient(90deg,#f6f6f6,#c9d3e2 50%,#f2f2f2)}
.thumb.network{background:linear-gradient(135deg,#8fd0f2,#2e8fd3 55%,#bfe6fa)}
.divider{position:absolute;left:102px;top:868px;width:934px;height:1px;background:#e3e3e3}
.intro{position:absolute;left:140px;top:906px;width:858px;text-align:center}
.intro h2{font-weight:300;font-size:25.5px;color:#333;line-height:34px}
.intro p{font-weight:300;font-size:12.5px;line-height:21px;color:var(--text);margin-top:9px}
.site-footer{position:absolute;left:0;top:1093px;width:1138px;height:107px;background:var(--footer-bg);border-top:1px solid #e6e6e6}
.footer-nav{position:absolute;left:104px;top:30px;font-size:14px;letter-spacing:-.4px;color:#333;white-space:nowrap}
.footer-nav a{color:#333;text-decoration:none}
.footer-nav .sep{margin:0 7px;color:#555}
.copyright{position:absolute;left:104px;top:64px;font-weight:300;font-size:12px;color:#666}
.social-foot{position:absolute;left:937px;top:31px;display:flex;gap:6px}
.social-foot span{width:26px;height:26px;border-radius:3px;background:var(--social-blue)}
</style>
</head>
<body>
<div class="hero-band"></div>

<header>
  <div class="brand">VORO</div>
  <div class="social-top" aria-label="Social links"><span></span><span></span><span></span><span></span></div>
  <nav class="main-nav">
    <a href="#" style="width:96px">Home</a>
    <a href="#" style="width:107px">About Us</a>
    <a href="#" style="width:102px">Services</a>
    <a href="#" style="width:100px">Telecom</a>
    <a href="#" style="width:155px">Launching Soon</a>
    <a href="#" style="width:77px">Blog</a>
    <a href="#" style="width:85px">News</a>
    <a href="#" style="width:101px">Support</a>
    <a href="#" style="width:111px">Contact</a>
  </nav>
</header>

<section class="hero">
  <svg class="arrow prev" width="40" height="100" viewBox="0 0 40 100"><polyline points="38,1 2,50 38,99" fill="none" stroke="#9a9a9a" stroke-width="1.5"/></svg>
  <div class="hero-visual" role="img" aria-label="Smartphone showing market data beside colourful rising bar blocks and a red growth arrow"></div>
  <h1 class="hero-title">Best Telecom Services Provider</h1>
  <h2 class="hero-sub">Curabitur vel mi sit amet magna malesuada</h2>
  <p class="hero-text">Vivamus porttitor, g, purus nisi eleifend libero, a tempus libero lectus feugiat felis. Morbi diam mauris, viverra in, gravida eu.</p>
  <div class="pager"><span class="active"></span><span></span><span></span></div>
  <svg class="arrow next" width="40" height="100" viewBox="0 0 40 100"><polyline points="2,1 38,50 2,99" fill="none" stroke="#9a9a9a" stroke-width="1.5"/></svg>
</section>

<section class="cards">
  <article class="card">
    <div class="thumb office" role="img" aria-label="Customer talking on a phone in an office"></div>
    <h3>Telecom Services</h3>
    <p>Mauris neque metus malesuada nec</p>
  </article>
  <article class="card">
    <div class="thumb support" role="img" aria-label="Support agent wearing a headset"></div>
    <h3>Services We Provide</h3>
    <p>Mauris neque metus malesuada nec</p>
  </article>
  <article class="card">
    <div class="thumb handsets" role="img" aria-label="Three touchscreen handsets side by side"></div>
    <h3>Mobile Lauching Soon</h3>
    <p>Mauris neque metus malesuada nec</p>
  </article>
  <article class="card">
    <div class="thumb network" role="img" aria-label="Laptop and phones connected on a blue network background"></div>
    <h3>Network Cabling</h3>
    <p>Mauris neque metus malesuada nec</p>
  </article>
</section>

<div class="divider"></div>

<section class="intro">
  <h2>Phasellus felis dolor scelerisque tempus eget lobortis</h2>
  <p>Phasellus felis dolor, scelerisque a, tempus eget, lobortis id, libero. Donec scelerisque leo ac risus. Praesent sit amet est. In dictum, dolor eu dictum porttitor, enim felis viverra mi, eget luctus massa purus quis odio. Etiam nulla massa, pharetra facilisis, volutpat in, imperdiet sit amet, sem.<br>Aliquam nec erat at purus cursus interdum. Vestibulum ligula augue, bibendum accumsan, vestibulum ut, commodo a, mi. Morbi ornare gravida elit. Integer congue, augue et malesuada iaculis, ipsum dui aliquet felis, at cursus magna nisl nec</p>
</section>

<footer class="site-footer">
  <nav class="footer-nav">
    <a href="#">HOME</a><span class="sep">|</span><a href="#">ABOUT US</a><span class="sep">|</span><a href="#">SERVICES</a><span class="sep">|</span><a href="#">TELECOM</a><span class="sep">|</span><a href="#">LAUNCHING SOON</a><span class="sep">|</span><a href="#">BLOG</a><span class="sep">|</span><a href="#">NEWS</a><span class="sep">|</span><a href="#">SUPPORT</a><span class="sep">|</span><a href="#">CONTACT</a>
  </nav>
  <div class="copyright">© 2013 Company Name.&nbsp; All right reserved.&nbsp; Term of Use</div>
  <div class="social-foot" aria-label="Social links"><span></span><span></span><span></span></div>
</footer>
</body>
</html>
```